New modern business card design

To design a brand new business card that's clean & modern in terms of layout.
I have attached our company logo and also basic information regarding what is needed on the card that also needs to be editable.

Target Market(s)

motor trade

Contact Information for Business Card

logo, name, title, tel, mob, email, address, www, all information is in the word.doc file

Requirements
Must have
• white background
Nice to have
• Nice clean font

```html
<!DOCTYPE html>
<html lang="en">
<head>
<meta charset="utf-8">
<title>Northgate Fixings Ltd – Business Card</title>
<link href="https://fonts.googleapis.com/css2?family=Oswald:wght@600&family=Roboto:wght@300;400;500&display=swap" rel="stylesheet">
<style>
  :root {
    --brand-blue: #1576be;
    --swoosh-grey: #a7a9ac;
    --backdrop: #bcbdc0;
    --card-white: #ffffff;
    --text-dark: #333333;
    --text-muted: #9a9c9f;
  }
  * { margin: 0; padding: 0; box-sizing: border-box; }
  html, body { width: 1038px; height: 1200px; overflow: hidden; }
  body { background: var(--backdrop); position: relative; font-family: "Roboto", sans-serif; }

  .card {
    position: absolute;
    left: 73px;
    width: 905px;
    height: 516px;
    background: var(--card-white);
    overflow: hidden;
    box-shadow: 14px 16px 22px rgba(0,0,0,0.35);
  }
  .card--front { top: 60px; background: var(--brand-blue); }
  .card--back { top: 614px; }
  .card svg.card-art { position: absolute; inset: 0; width: 100%; height: 100%; }

  .front-brand {
    position: absolute;
    left: 0; right: 0;
    top: 196px;
    text-align: center;
    color: var(--card-white);
    font-weight: 400;
    font-size: 44px;
    letter-spacing: 2px;
    line-height: 1.15;
  }

  .holder { position: absolute; left: 50px; top: 50px; }
  .holder-name {
    font-family: "Oswald", sans-serif;
    font-weight: 600;
    font-size: 31px;
    letter-spacing: 1.5px;
    color: var(--brand-blue);
    line-height: 36px;
    padding-bottom: 4px;
    border-bottom: 2px solid var(--brand-blue);
    width: 178px;
    white-space: nowrap;
  }
  .holder-title {
    margin-top: 6px;
    font-weight: 300;
    font-size: 21px;
    color: var(--text-muted);
    letter-spacing: 0.5px;
  }

  .back-brand {
    position: absolute;
    right: 76px;
    top: 68px;
    text-align: center;
    color: var(--brand-blue);
    font-weight: 400;
    font-size: 21px;
    letter-spacing: 1px;
    line-height: 1.2;
  }

  .contact-list { position: absolute; left: 53px; top: 232px; list-style: none; }
  .contact-item {
    display: flex;
    align-items: center;
    height: 41.5px;
    font-size: 23px;
    color: var(--text-dark);
  }
  .contact-icon { width: 32px; height: 32px; margin-right: 13px; flex: none; }

  .web-link {
    position: absolute;
    left: 264px;
    top: 466px;
    display: flex;
    align-items: center;
    color: var(--card-white);
    font-size: 23px;
  }
  .web-link svg { width: 26px; height: 26px; margin-right: 14px; }
</style>
</head>
<body>

<section class="card card--front">
  <svg class="card-art" viewBox="0 0 905 516" preserveAspectRatio="none" aria-hidden="true">
    <path d="M0,0 C20,300 250,490 640,516 L0,516 Z" fill="var(--swoosh-grey)"/>
    <path d="M0,55 C30,330 240,492 570,516 L0,516 Z" fill="var(--card-white)"/>
  </svg>
  <div class="front-brand">NORTHGATE FIXINGS<br>LTD</div>
</section>

<section class="card card--back">
  <svg class="card-art" viewBox="0 0 904 515" preserveAspectRatio="none" aria-hidden="true">
    <polygon points="0,0 26,0 26,119 0,95" fill="var(--brand-blue)"/>
    <path d="M0,515 Q452,290 904,515 Z" fill="var(--swoosh-grey)"/>
    <path d="M0,515 Q452,332 904,515 Z" fill="var(--card-white)"/>
    <path d="M0,515 Q452,352 904,515 Z" fill="var(--brand-blue)"/>
  </svg>

  <div class="holder">
    <div class="holder-name">DANIEL HARWOOD</div>
    <div class="holder-title">GENERAL MANAGER</div>
  </div>

  <div class="back-brand">NORTHGATE FIXINGS<br>LTD</div>

  <ul class="contact-list">
    <li class="contact-item">
      <svg class="contact-icon" viewBox="0 0 32 32" aria-hidden="true">
        <circle cx="16" cy="16" r="16" fill="var(--brand-blue)"/>
        <path d="M8,14 Q16,8 24,14 L22,16 L19,15 L19,13 Q16,12 13,13 L13,15 L10,16 Z M11,17 L21,17 L23,23 L9,23 Z" fill="#fff"/>
      </svg>
      0161 555 0142
    </li>
    <li class="contact-item">
      <svg class="contact-icon" viewBox="0 0 32 32" aria-hidden="true">
        <circle cx="16" cy="16" r="16" fill="var(--brand-blue)"/>
        <path d="M11,8 L14,12 L12,14 Q14,18 18,20 L20,18 L24,21 L22,24 Q16,25 11,20 Q7,15 8,10 Z" fill="#fff"/>
      </svg>
      07700 900 418
    </li>
    <li class="contact-item">
      <svg class="contact-icon" viewBox="0 0 32 32" aria-hidden="true">
        <circle cx="16" cy="16" r="16" fill="var(--brand-blue)"/>
        <rect x="8" y="11" width="16" height="11" fill="#fff"/>
        <path d="M8,11 L16,17 L24,11" fill="none" stroke="var(--brand-blue)" stroke-width="1.3"/>
      </svg>
      dharwood@northgate-fixings.co.uk
    </li>
    <li class="contact-item">
      <svg class="contact-icon" viewBox="0 0 32 32" aria-hidden="true">
        <circle cx="16" cy="16" r="16" fill="var(--brand-blue)"/>
        <path d="M16,7 A6.5,6.5 0 0 1 22.5,13.5 Q22.5,18 16,25 Q9.5,18 9.5,13.5 A6.5,6.5 0 0 1 16,7 Z" fill="none" stroke="#fff" stroke-width="1.8"/>
        <circle cx="16" cy="13.5" r="2.4" fill="#fff"/>
      </svg>
      Mill Lane Denton, Northfield NF4 2QD
    </li>
  </ul>

  <div class="web-link">
    <svg viewBox="0 0 26 26" aria-hidden="true">
      <g fill="none" stroke="#fff" stroke-width="1.6">
        <circle cx="13" cy="13" r="11"/>
        <ellipse cx="13" cy="13" rx="5" ry="11"/>
        <line x1="2" y1="13" x2="24" y2="13"/>
        <line x1="4" y1="7.5" x2="22" y2="7.5"/>
        <line x1="4" y1="18.5" x2="22" y2="18.5"/>
      </g>
    </svg>
    WWW.NORTHGATE-FIXINGS.CO.UK
  </div>
</section>

</body>
</html>
```